Construction Company Website Design

I need a Website Design for a Construction Company. I have attached logo and business card design files (a.i) to match styles and text for the website. I will need design for 3 pages:
1. A Home page
2. A secondary page (will be different information pages)
3. A contact page with submision form
Website to look professional and match the 'theme' across all pages, using main colours / reverse colours as per design files. Must be clear it is a construction related website without being over the top. Happy for the construction related details (whether that be images/outlines/backgrounds etc to be fairly subtle and not overbearing on the contect of the pages. It will be the content that will be most important, not the images within.

Content has not yet been fully completed but attached is a site map. Each page will need a space for the insertion of the relevant heading and associated content for that particular page. Example can be used as per attached map. If it is preferable to have content completed for this to be a more succesful project please advise and I will complete and submit.

Target Market(s)

Clients for potential construction projects. These could be a range of people. All would be very professional, well educated and put a substantial expection on the quality of website provided.

Industry/Entity Type

Construction

Number of Pages Required

3 page

Font styles to use
Serif
Sans Serif
Other font styles liked:
• fonts preferable as per design files provided unless designer beleives a different font would suit better

Requirements
Must have
• Colour scheme to match logo and business card files provided. Fonts that match as per provided files. Pages must be consistent with the theme carrying across all pages. All pages must have contact details at the bottom of the page.
• Contents of page 1 - 'Home page': multiple tab options / logo link
• Contents of page 2 - 'Secondary page': Top and side navigation / area for information and/or images.
• Contents of page - 'Contact us page': Top and side navigation / Submission form / area for logos such as linkdin, facebook etc.
Nice to have
• Would be good to have a or some generic construction related images - outlines / shadows / effects etc. These might be background images or outlines related to the relevant industry and are consistent across the pages. Could be outlines of buildings, images of men with hardhats etc etc. Good to see colour scheme as per design files used
Should not have
• No pictures of houses. Generally no photos. If any imagery of people must not show faces/details.

```html
<!DOCTYPE html>
<html lang="en">
<head>
<meta charset="utf-8">
<title>K.R.T Constructions</title>
<link href="https://fonts.googleapis.com/css2?family=Montserrat:wght@400;600;700&family=Open+Sans:wght@400;600;700&display=swap" rel="stylesheet">
<style>
:root{
  --blue:#1d9be3;
  --blue-dark:#0f6fae;
  --ink:#2b2b2b;
  --text:#3d3d3d;
  --white:#ffffff;
  --news-bg:#a3a3a3;
  --footer-bg:#3a3a3a;
  --footer-bar:#2c2c2c;
  --muted:#d0d0d0;
}
*{box-sizing:border-box;margin:0;padding:0}
html,body{width:1200px;height:2356px;overflow:hidden}
body{position:relative;background:var(--white);font-family:"Open Sans",Arial,sans-serif;color:var(--text)}
.abs{position:absolute}
.btn{position:absolute;background:var(--blue);color:var(--white);font:600 15px "Open Sans",Arial,sans-serif;text-align:center;border-radius:4px;line-height:34px;height:34px}

/* hero */
.hero{left:0;top:0;width:1200px;height:625px;background:linear-gradient(180deg,#1f4f86 0%,#3f7fb8 35%,#c9a15a 70%,#3b3d44 100%)}
.topbar{left:0;top:0;width:1200px;height:54px;background:rgba(10,20,40,.55)}
.brand{left:30px;top:14px;display:flex;align-items:center;gap:10px;color:var(--white);font:600 20px "Montserrat",Arial,sans-serif;line-height:26px}
.brand .mark{width:14px;height:14px;background:var(--white)}
.nav{right:30px;top:18px;display:flex;gap:22px;font:600 13px "Montserrat",Arial,sans-serif;color:var(--white)}
.nav .active{color:var(--blue)}
.arrow{top:300px;width:24px;height:40px}
.dots{left:585px;top:592px;display:flex;gap:8px}
.dots span{width:12px;height:12px;border-radius:50%;background:rgba(255,255,255,.5)}
.dots span.on{background:var(--white)}

/* sections */
h2{font:700 26px "Montserrat",Arial,sans-serif;color:var(--ink);letter-spacing:1px;white-space:nowrap}
h2 em{font-style:normal;color:var(--blue)}
.copy{font-size:18px;line-height:26px;color:var(--text)}

/* location */
.location{left:0;top:1345px;width:1200px;height:370px;background:linear-gradient(135deg,#173b63 0%,#6fa4cf 45%,#c6dff0 70%,#5d8db5 100%)}
.loc-card{left:122px;top:1420px;width:480px;height:295px;background:rgba(40,40,45,.78);padding:30px 28px;color:var(--white)}
.loc-card h3{font:700 22px "Montserrat",Arial,sans-serif;color:var(--blue);margin-bottom:18px;letter-spacing:1px}
.loc-card p{font-size:16px;line-height:26px}

/* news */
.news{left:0;top:1715px;width:1200px;height:305px;background:var(--news-bg)}
.news h3{position:absolute;left:130px;top:12px;font:700 24px "Montserrat",Arial,sans-serif;color:var(--blue)}
.card{top:1780px;width:202px;height:210px;background:var(--white);padding:14px 14px;font-size:11px;line-height:15px;color:#555}
.card .handle{color:var(--blue);font-weight:600;margin-bottom:8px}
.card .link{color:var(--blue);margin-top:6px}
.card .dot{position:absolute;right:14px;bottom:12px;width:16px;height:16px;border-radius:50%;background:var(--blue)}
.promo{left:822px;top:1775px;width:258px;height:215px}

/* footer */
.footer{left:0;top:2020px;width:1200px;height:336px;background:var(--footer-bg);color:var(--white)}
.fnav{left:50px;top:2110px;display:flex;gap:10px;font:600 12px "Montserrat",Arial,sans-serif;color:var(--white)}
.fhead{font:600 14px "Montserrat",Arial,sans-serif;color:var(--white)}
.fcontact{left:672px;top:2066px;font-size:13px;line-height:19px;color:var(--muted)}
.social{left:960px;top:2066px}
.social .row{display:flex;gap:8px;margin-top:10px}
.social .row span{width:24px;height:24px;border-radius:2px}
.fbar{left:0;top:2320px;width:1200px;height:36px;background:var(--footer-bar);font-size:12px;color:var(--muted);line-height:36px}
</style>
</head>
<body>

<div class="abs hero" role="img" aria-label="Photo of tower cranes over a building under construction at sunrise"></div>
<div class="abs topbar"></div>
<div class="abs brand"><span class="mark"></span><span>K.R.T Constructions</span></div>
<nav class="abs nav">
  <span class="active">HOME</span><span>ABOUT US</span><span>SERVICES &#9662;</span><span>PROJECTS</span><span>CULTURE</span><span>NEWS</span><span>CONTACT</span>
</nav>
<svg class="abs arrow" style="left:20px" viewBox="0 0 24 40"><path d="M18 4 L6 20 L18 36" fill="none" stroke="rgba(255,255,255,.7)" stroke-width="3"/></svg>
<svg class="abs arrow" style="right:20px" viewBox="0 0 24 40"><path d="M6 4 L18 20 L6 36" fill="none" stroke="rgba(255,255,255,.7)" stroke-width="3"/></svg>
<div class="abs dots"><span class="on"></span><span></span><span></span></div>

<section>
  <div class="abs" style="left:74px;top:660px;width:468px;height:310px;background:linear-gradient(135deg,#e9eef3,#b8c7d5)" role="img" aria-label="Photo of a builder in a hard hat reviewing plans"></div>
  <h2 class="abs" style="left:628px;top:722px">WHO IS <em>K.R.T CONSTRUCTIONS</em>?</h2>
  <p class="abs copy" style="left:660px;top:778px;width:440px">Lorem ipsum dolor sit amet, consectetur adipiscing elit. Aenean euismod bibendum laoreet. Proin gravida dolor sit amet lacus accumsan et viverra justo commodo.</p>
  <div class="btn" style="left:805px;top:900px;width:122px">About us</div>
</section>

<section>
  <h2 class="abs" style="left:150px;top:1078px">OUR <em>WINNING PROJECTS</em></h2>
  <p class="abs copy" style="left:130px;top:1130px;width:440px">Lorem ipsum dolor sit amet, consectetur adipiscing elit. Aenean euismod bibendum laoreet. Proin gravida dolor sit amet lacus accumsan et viverra justo commodo.</p>
  <div class="btn" style="left:264px;top:1256px;width:122px">Projects</div>
  <div class="abs" style="left:640px;top:1012px;width:462px;height:312px;background:linear-gradient(180deg,#cfe3f3 0%,#9fb8cc 60%,#5f8a4e 100%)" role="img" aria-label="Photo of completed high-rise buildings with lawn in front"></div>
</section>

<div class="abs location" role="img" aria-label="Photo of a modern glass office building"></div>
<div class="abs loc-card">
  <h3>LOCATION</h3>
  <p>K.R.T Constructions Pty Limited<br>14 Ridge Avenue<br>Harbour Vale 2091</p>
  <div class="btn" style="left:28px;top:232px;width:225px;border-radius:2px">Map Our Location
    <svg width="14" height="18" viewBox="0 0 14 18" style="vertical-align:middle;margin-left:10px"><path d="M7 0C3 0 0 3 0 7c0 5 7 11 7 11s7-6 7-11c0-4-3-7-7-7z" fill="#fff"/><circle cx="7" cy="7" r="2.5" fill="#1d9be3"/></svg>
  </div>
</div>

<div class="abs news"><h3>NEWS</h3></div>
<div class="abs card" style="left:130px">
  <div class="handle">@krtconstruct</div>
  <p>Lorem ipsum dolor sit amet, consectetur adipiscing elit. Aenean euismod bibendum laoreet. Proin gravida dolor sit amet lacus.</p>
  <p class="link">krtconstruct.com.au/news</p><span class="dot"></span>
</div>
<div class="abs card" style="left:360px">
  <div class="handle">@krtconstruct</div>
  <p>Lorem ipsum dolor sit amet, consectetur adipiscing elit. Aenean euismod bibendum laoreet. Proin gravida dolor sit amet lacus.</p>
  <p class="link">krtconstruct.com.au/news</p><span class="dot"></span>
</div>
<div class="abs card" style="left:590px">
  <div class="handle">@krtconstruct</div>
  <p>Lorem ipsum dolor sit amet, consectetur adipiscing elit. Aenean euismod bibendum laoreet. Proin gravida dolor sit amet lacus.</p>
  <p class="link">krtconstruct.com.au/news</p><span class="dot"></span>
</div>
<div class="abs promo">
  <div style="height:110px;background:linear-gradient(135deg,#e0b14a,#8a6a3a)" role="img" aria-label="Photo of builders on site in hard hats"></div>
  <div style="height:105px;background:var(--blue);color:#fff;padding:14px 16px;font:600 15px/20px 'Open Sans',Arial,sans-serif">Sign up to receive<br>K.R.T Construction News
    <div style="margin-top:12px;display:inline-block;background:var(--blue-dark);padding:2px 12px;font-size:12px">Read more &#9656;</div>
  </div>
</div>

<footer class="abs footer"></footer>
<div class="abs brand" style="top:2062px;left:50px"><span class="mark"></span><span>K.R.T Constructions</span></div>
<div class="abs fnav"><span>HOME</span>|<span>ABOUT US</span>|<span>SERVICES</span>|<span>PROJECTS</span>|<span>CULTURE</span>|<span>NEWS</span>|<span>CONTACT</span></div>
<div class="abs fcontact">
  <div class="fhead" style="margin-bottom:10px">CONTACT</div>
  K.R.T Constructions Pty Limited<br>14 Ridge Avenue<br>Harbour Vale 2091<br><br>0400 555 017
</div>
<div class="abs social">
  <div class="fhead">CONNECT WITH US</div>
  <div class="row"><span style="background:#3b5998"></span><span style="background:#1da1f2"></span><span style="background:#d62d20"></span><span style="background:#0e76a8"></span></div>
</div>
<div class="abs fbar">
  <span style="margin-left:50px">All contents &copy;2016 K.R.T Constructions Pty Limited. All rights reserved.</span>
  <span style="position:absolute;right:50px">SITE MAP &nbsp;&bull;&nbsp; PRIVACY POLICY</span>
</div>

</body>
</html>
```